Cover for "TANDEM! The skill and rhythm of guiding teams through calm and delight"

My first book for a global audience of modern performance leaders needs its cover!
I am an international executive coach and I've developed a new approach to replace classic Performance Management with a natural, sustainable approach fit for human beings :) My first book is about this approach and serves two purposes: helping leaders and sparking their curiosity to learn more, and positioning myself as a thought leader in the field.
The book is built on personal experience; it is both professional and personal ("From me to You"), and I'd like to position it beyond classic categorisation.
Its cover should communicate humanness, naturalness, ease and joy, within an unmistakably business-y context. I would like to see designs that use the color yellow (but not sure it communicates the right things).
Updates

Sick

Target Market(s)

Leaders who aspire to have a positive impact and deliver results in a meaningful way

Industry/Entity Type

Consulting & Executive Coaching - Trusted Advisor

Font styles to use
Other font styles liked:
• Helvetica Neue

Colors
0094D4
00A9DD
6FCCEA
C7EBF8
E9F6FB
FFC000
F8CF3A
FAE287
FDF2CF
FEFAEE
EE7325
F08F49
F5BC92
FAE3D3
FDF4ED

Requirements
Must have
• A both-and feeling to it (see description), e.g., masculine AND feminine, business AND humanness. Power with, not power over...
Should not have
• Too much "bling" - no classic status symbol business success language

```html
<!DOCTYPE html>
<html lang="en">
<head>
<meta charset="utf-8">
<title>TANDEM — Book Cover</title>
<link rel="stylesheet" href="https://fonts.googleapis.com/css2?family=Arimo:wght@400;500;700&display=swap">
<style>
  :root {
    --cover-yellow: #F5BF27;
    --title-purple: #2C0F4B;
    --text-olive: #5A4617;
  }
  * { margin: 0; padding: 0; box-sizing: border-box; }
  html, body {
    width: 752px;
    height: 1200px;
    overflow: hidden;
    background: var(--cover-yellow);
  }
  .cover {
    position: relative;
    width: 752px;
    height: 1200px;
    background: var(--cover-yellow);
    font-family: "Arimo", "Helvetica Neue", Helvetica, Arial, sans-serif;
    color: var(--text-olive);
  }
  .cover__subtitle {
    position: absolute;
    top: 62px;
    left: 0;
    width: 100%;
    text-align: center;
    font-size: 30px;
    line-height: 44px;
    font-weight: 400;
    letter-spacing: -0.2px;
  }
  .cover__title {
    position: absolute;
    top: 394px;
    left: 0;
    width: 100%;
    text-align: center;
    font-size: 150px;
    line-height: 150px;
    font-weight: 700;
    letter-spacing: 6px;
    padding-left: 6px;
    color: var(--title-purple);
    white-space: nowrap;
  }
  .cover__tagline {
    position: absolute;
    top: 848px;
    left: 0;
    width: 100%;
    text-align: center;
    text-transform: uppercase;
    font-size: 30px;
    line-height: 45px;
    font-weight: 400;
    letter-spacing: -0.6px;
  }
  .cover__author {
    position: absolute;
    top: 1108px;
    left: 0;
    width: 100%;
    text-align: center;
    font-size: 44px;
    line-height: 1;
    font-weight: 500;
    letter-spacing: 0.45em;
    padding-left: 0.45em;
    text-transform: uppercase;
  }
</style>
</head>
<body>
  <main class="cover">
    <p class="cover__subtitle">Team Leadership with a Calm and Steady<br>and Human-Centred rhythm<br>made for Real People</p>

    <h1 class="cover__title">TANDEM</h1>

    <p class="cover__tagline">The skill and rhythm of<br>guiding teams through<br>calm and delight</p>

    <p class="cover__author">Author Name</p>
  </main>
</body>
</html>
```